Branvique needs a business Card Design

We are looking for a business card Design for our new Managed Service Provider Company, Branvique. Branvique encompasses everything IT for the average medium sized business. Our primary services are help desk support, cyber-security (malware and ransomware protection), and Disaster Recovery systems. We would like the design to have a very clean and professional look, with a very minimalist feel.

Target Market(s)

Medium to large sized businesses

Industry/Entity Type

It Service

Contact Information for Business Card

Name GoesHere
name@branvique.com
O: 555-382-6047
C: 555-731-5820

Font styles to use
Other font styles liked:
• Poppins Font Only Please

Colors

Designer to choose only greyscale colors for use in the design.

Requirements
Must have
• Logo included
Nice to have
• Cutting Edge, innovative, minimalistic, elegant

```html
<!DOCTYPE html>
<html lang="en">
<head>
<meta charset="utf-8">
<title>Branvique Business Card</title>
<link href="https://fonts.googleapis.com/css2?family=Poppins:wght@300;400;700&display=swap" rel="stylesheet">
<style>
  :root {
    --stage: #3a3a3a;
    --paper: #ffffff;
    --charcoal: #1c1c1c;
    --ink: #1e1e1e;
    --text: #444444;
    --rule: #bdbdbd;
    --white: #ffffff;
    --soft-white: #e6e6e6;
  }
  * { box-sizing: border-box; margin: 0; padding: 0; }
  html, body {
    width: 1200px; height: 970px; overflow: hidden;
    background: var(--stage);
    font-family: "Poppins", sans-serif;
  }
  .canvas { position: relative; width: 1200px; height: 970px; }
  .card {
    position: absolute; width: 620px; height: 354px;
    box-shadow: 0 14px 30px rgba(0,0,0,.45);
  }
  .card--front { left: 90px; top: 90px; background: var(--paper); color: var(--ink); }
  .card--back { left: 490px; top: 526px; background: var(--charcoal); color: var(--white); }

  .brand { position: absolute; display: flex; flex-direction: column; align-items: center; }
  .brand__mark { width: 22px; height: 22px; background: currentColor; margin-bottom: 18px; }
  .brand__name {
    font-weight: 300; letter-spacing: .38em; text-transform: uppercase;
    padding-left: .38em; white-space: nowrap; line-height: 1;
  }
  .card--front .brand { left: 30px; top: 100px; width: 264px; }
  .card--front .brand__name { font-size: 24px; }
  .card--back .brand { left: 0; right: 0; top: 100px; }
  .card--back .brand__mark { width: 28px; height: 28px; margin-bottom: 24px; }
  .card--back .brand__name { font-size: 34px; }

  .divider { position: absolute; left: 314px; top: 82px; width: 1px; height: 150px; background: var(--rule); }

  .contact { position: absolute; left: 340px; top: 70px; }
  .contact__name { font-size: 24px; font-weight: 700; color: var(--ink); line-height: 1.15; }
  .contact__title { font-size: 14px; color: var(--text); margin-bottom: 14px; }
  .contact__list { list-style: none; }
  .contact__item {
    display: flex; align-items: center; gap: 14px;
    font-size: 15px; color: var(--text); line-height: 1.7; white-space: nowrap;
  }
  .contact__icon { width: 15px; height: 15px; fill: var(--ink); flex: none; }

  .services {
    position: absolute; left: 0; right: 0; bottom: 34px;
    text-align: center; font-size: 15px; color: var(--text); white-space: nowrap;
  }
  .services__sep { margin: 0 9px; color: var(--rule); }

  .website {
    position: absolute; left: 0; right: 0; top: 250px;
    text-align: center; font-size: 16px; letter-spacing: .03em; color: var(--soft-white);
  }
</style>
</head>
<body>
<main class="canvas">
  <section class="card card--front" aria-label="Business card front">
    <div class="brand">
      <span class="brand__mark"></span>
      <span class="brand__name">Branvique</span>
    </div>
    <div class="divider"></div>
    <div class="contact">
      <p class="contact__name">GoesHere</p>
      <p class="contact__title">Founder &amp; CEO</p>
      <ul class="contact__list">
        <li class="contact__item">
          <svg class="contact__icon" viewBox="0 0 16 16"><path d="M1 5c0-2 2-3 7-3s7 1 7 3v1h-4V5H5v1H1z"/><rect x="3" y="7" width="10" height="7" rx="1"/></svg>
          555-382-6047
        </li>
        <li class="contact__item">
          <svg class="contact__icon" viewBox="0 0 16 16"><path d="M4 1h8a1 1 0 0 1 1 1v12a1 1 0 0 1-1 1H4a1 1 0 0 1-1-1V2a1 1 0 0 1 1-1zm1 2v9h6V3zm3 10a.8.8 0 1 0 0 .01z"/></svg>
          555-731-5820
        </li>
        <li class="contact__item">
          <svg class="contact__icon" viewBox="0 0 16 16"><path d="M1 3h14v10H1zm1 1.2V5l6 4 6-4v-.8L8 8z"/></svg>
          name@branvique.com
        </li>
      </ul>
    </div>
    <p class="services">Help desk support<span class="services__sep">|</span>Cyber-security<span class="services__sep">|</span>Disaster Recovery systems</p>
  </section>

  <section class="card card--back" aria-label="Business card back">
    <div class="brand">
      <span class="brand__mark"></span>
      <span class="brand__name">Branvique</span>
    </div>
    <p class="website">www.branvique.com</p>
  </section>
</main>
</body>
</html>
```